KDP Mortgage Flyer

We are a mortgage company, advertising for he KDP quickpath program. I would like the following information to be included on the post card:
Most of this information should be on one side of the card
LOWER YOUR KDP MORTGAGE PAYMENT RIGHT NOW

Using the KDP Quickpath program you might be eligible to lower your interest rate and monthly mortgage insurance (MIP) at zero cost to you
The KDP has dramatically reduced its restrictions on Mortgage Insurance Premiums (MIP), combined with rates at historic lows, now is the time to take advantage of the KDP Quickpath Program.

The Quickpath process requires NO APPRAISAL, NO INCOME VERIFICATION, NO ASSET DOCUMENTATION and NO OUT OF POCKET CLOSING COSTS.
What this means to you is:
A REDUCTION IN MONTHLY PAYMENT
POSSIBILITY TO SKIP FIRST TWO MORTGAGE PAYMENTS
SAME TYPE OF 30 YEAR FIXED RATE LOAN – BACKED BY THE KDP
*To qualify for the KDP QUICKPATH you must have a good payment history with zero late payments in the past 12 months

I would like to include our logos on both sides, one side should have the TRC logo as well.
Please have our contact info displayed prominently on both sides
the contact information is as follows and all must be included

Quillan Mortgage
418 Garnet Avenue, Suite 1450
Seattle, WA 98344
Office 206 555 0143
Fax 206 555 0187
Email quickpath@quillanmortgage.com
Tom Wendell - Vice President - MLO-31947
Leo Marsh - Loan Originator

If you could please make the postcard colorful as well as adding some appropriate artwork (home, fence, yard etc) that would be great
thanks so much

```html
<!DOCTYPE html>
<html lang="en">
<head>
<meta charset="utf-8">
<title>KDP Quickpath Mortgage Flyer and Postcard</title>
<link href="https://fonts.googleapis.com/css2?family=Lato:wght@700;900&family=Open+Sans:wght@400;600&family=Pathway+Gothic+One&display=swap" rel="stylesheet">
<style>
:root{
  --stage:#161616;
  --green:#5a9e34;
  --green-dark:#3f7d22;
  --green-light:#7bbd4a;
  --wood:#7a6550;
  --wood-dark:#5a4939;
  --ink:#2b2b2b;
  --paper:#ffffff;
  --badge:#2f5f7a;
  --pin:#d4221c;
}
*{margin:0;padding:0;box-sizing:border-box}
html,body{width:960px;height:1200px;overflow:hidden;background:var(--stage)}
.canvas{position:relative;width:960px;height:1200px;background:var(--stage)}
.abs{position:absolute}
.title{font-family:"Lato",sans-serif;font-weight:900;color:var(--paper);font-size:19px;line-height:23px;letter-spacing:.2px;white-space:nowrap}
.cond{font-family:"Pathway Gothic One",sans-serif}
.brand{font-family:"Open Sans",sans-serif;font-weight:600;color:var(--green-dark);font-size:13px;display:flex;align-items:center;gap:5px}
.brand i{display:block;width:9px;height:9px;border-radius:50%;background:var(--green)}
.badge{width:23px;height:17px;background:var(--badge);border-radius:2px}

/* flyer */
.flyer{left:271px;top:90px;width:403px;height:621px;overflow:hidden;background:var(--wood)}
.flyer .header{left:0;top:0;width:403px;height:57px;background:var(--green);padding:8px 16px}
.flyer .photo{left:0;top:57px;width:403px;height:250px;background:linear-gradient(135deg,#8fb56a 0%,#d9c3a6 45%,#c9a98a 70%,#9dbb7e 100%)}
.flyer .fence{left:0;top:290px;width:403px;height:331px;background:linear-gradient(90deg,var(--wood-dark),var(--wood) 30%,#8d7760 60%,var(--wood-dark))}
.flyer .swoosh{left:0;top:225px}
.flyer .intro{left:16px;top:306px;width:190px;height:140px;background:var(--paper);padding:6px 10px 0 11px;font-family:"Open Sans",sans-serif;font-size:9.6px;line-height:11.8px;color:var(--ink)}
.flyer .means-head{left:212px;top:302px;width:191px;height:22px;background:rgba(235,225,210,.85);font-family:"Open Sans",sans-serif;font-size:12px;color:var(--ink);padding:3px 0 0 7px;white-space:nowrap}
.flyer .means{left:214px;top:336px;width:190px;list-style:none}
.flyer .means li{display:flex;gap:4px;font-size:12px;line-height:13px;color:var(--paper);margin-bottom:13px}
.flyer .req-head{left:12px;top:460px;width:193px;height:27px;background:var(--green);color:var(--paper);font-family:"Pathway Gothic One",sans-serif;font-size:16px;line-height:27px;padding:0 0 0 14px;white-space:nowrap}
.flyer .req{left:12px;top:490px;width:193px;height:74px;background:rgba(225,215,200,.55)}
.flyer .foot{left:0;top:570px;width:164px;height:51px;background:var(--paper)}

/* requirement block */
.no{font-family:"Pathway Gothic One",sans-serif;color:var(--paper);-webkit-text-stroke:1.2px var(--ink);line-height:1}
.checks{list-style:none}
.checks li{display:flex;justify-content:space-between;align-items:center;font-family:"Pathway Gothic One",sans-serif;color:var(--ink);white-space:nowrap}

/* contact note */
.note{background:var(--paper);box-shadow:2px 3px 6px rgba(0,0,0,.45);font-family:"Pathway Gothic One",sans-serif;color:var(--ink);white-space:nowrap}
.note .firm{color:var(--green-dark);font-size:13px}
.note p{font-size:9.6px;line-height:11px}
.note .staff{font-size:11px;line-height:12px;margin-top:6px}
.note .staff small{font-size:8px}
.note .pin{position:absolute;left:16px;top:-6px}

/* postcard */
.postcard{left:172px;top:772px;width:600px;height:390px;background:var(--paper);overflow:hidden}
.postcard .field{left:0;top:0}
.postcard .req-head{left:23px;top:84px;font-family:"Pathway Gothic One",sans-serif;font-size:20px;line-height:24px;color:var(--ink);white-space:nowrap}
.postcard .means-head{left:26px;top:216px;font-family:"Pathway Gothic One",sans-serif;font-size:17px;line-height:18px;color:var(--ink)}
.postcard .means{left:9px;top:260px;list-style:none;width:150px}
.postcard .means li{display:flex;gap:5px;font-size:9px;line-height:10px;color:var(--paper);margin-bottom:10px;white-space:nowrap}
.stamp{left:504px;top:22px;width:67px;height:67px;border:1px solid #cfcfcf}
.addr-line{left:363px;width:207px;height:1px;background:#e2e2e2}
</style>
</head>
<body>
<div class="canvas">

  <!-- Flyer -->
  <section class="abs flyer">
    <div class="abs photo" role="img" aria-label="Photo of a smiling family of four leaning on a wooden garden fence"></div>
    <div class="abs fence" role="img" aria-label="Weathered wooden fence boards"></div>
    <svg class="abs swoosh" width="403" height="80" viewBox="0 0 403 80">
      <path d="M0 12 Q200 70 403 18 L403 50 Q200 88 0 40 Z" fill="var(--green)"/>
      <path d="M0 40 Q200 88 403 50 L403 70 Q200 100 0 60 Z" fill="var(--green-dark)"/>
      <path d="M0 8 Q200 66 403 14 L403 20 Q200 72 0 14 Z" fill="#ffffff"/>
    </svg>
    <header class="abs header"><h1 class="title">LOWER YOUR KDP MORTGAGE<br>PAYMENT RIGHT NOW</h1></header>

    <p class="abs intro">Using the KDP Quickpath program you might be eligible to lower your interest rate and monthly mortgage insurance (MIP) at zero cost to you The KDP has dramatically reduced its restrictions on Mortgage Insurance Premiums (MIP), combined with rates at historic lows, now is the time to take advantage of the KDP Quickpath Program.</p>

    <div class="abs means-head">What this means to you is:</div>
    <ul class="abs means cond">
      <li><svg width="14" height="10" viewBox="0 0 14 10"><path d="M0 5h9M6 1l4 4-4 4" stroke="var(--green-light)" stroke-width="2.4" fill="none"/></svg>A REDUCTION IN MONTHLY PAYMENT</li>
      <li><svg width="14" height="10" viewBox="0 0 14 10"><path d="M0 5h9M6 1l4 4-4 4" stroke="var(--green-light)" stroke-width="2.4" fill="none"/></svg>POSSIBILITY TO SKIP FIRST TWO<br>MORTGAGE PAYMENTS</li>
      <li><svg width="14" height="10" viewBox="0 0 14 10"><path d="M0 5h9M6 1l4 4-4 4" stroke="var(--green-light)" stroke-width="2.4" fill="none"/></svg>SAME TYPE OF 30 YEAR<br>FIXED RATE LOAN – BACKED BY THE KDP</li>
    </ul>

    <div class="abs req-head">The Quickpath process requires</div>
    <div class="abs req">
      <span class="abs no" style="left:3px;top:4px;font-size:66px">NO</span>
      <ul class="abs checks" style="left:62px;top:6px;width:124px">
        <li style="font-size:11px;height:16px">APPRAISAL<svg width="9" height="9" viewBox="0 0 9 9"><rect x=".5" y=".5" width="8" height="8" fill="#fff" stroke="var(--green)"/><path d="M2 4.5l2 2 3-4" stroke="var(--green)" fill="none" stroke-width="1.3"/></svg></li>
        <li style="font-size:11px;height:16px">INCOME VERIFICATION<svg width="9" height="9" viewBox="0 0 9 9"><rect x=".5" y=".5" width="8" height="8" fill="#fff" stroke="var(--green)"/><path d="M2 4.5l2 2 3-4" stroke="var(--green)" fill="none" stroke-width="1.3"/></svg></li>
        <li style="font-size:11px;height:16px">ASSET DOCUMENTATION<svg width="9" height="9" viewBox="0 0 9 9"><rect x=".5" y=".5" width="8" height="8" fill="#fff" stroke="var(--green)"/><path d="M2 4.5l2 2 3-4" stroke="var(--green)" fill="none" stroke-width="1.3"/></svg></li>
        <li style="font-size:11px;height:16px">OUT OF POCKET CLOSING COSTS.<svg width="9" height="9" viewBox="0 0 9 9"><rect x=".5" y=".5" width="8" height="8" fill="#fff" stroke="var(--green)"/><path d="M2 4.5l2 2 3-4" stroke="var(--green)" fill="none" stroke-width="1.3"/></svg></li>
      </ul>
    </div>

    <div class="abs foot">
      <div class="abs badge" style="left:12px;top:13px"></div>
      <div class="abs brand" style="left:78px;top:17px"><i></i>Quillan</div>
    </div>

    <div class="abs note" style="left:226px;top:460px;width:168px;height:150px;padding:24px 10px 0 12px;transform:rotate(-4deg)">
      <svg class="pin" width="20" height="24" viewBox="0 0 20 24"><circle cx="9" cy="9" r="8" fill="var(--pin)"/><path d="M9 16l-3 8" stroke="#888" stroke-width="1.5"/></svg>
      <div class="firm">Quillan Mortgage</div>
      <p>418 Garnet Avenue, Suite 1450<br>Seattle, WA 98344<br>Office 206 555 0143<br>Fax 206 555 0187<br>Email quickpath@quillanmortgage.com</p>
      <div class="staff">Tom Wendell <small>- Vice President - MLO-31947</small><br>Leo Marsh <small>- Loan Originator</small></div>
    </div>
  </section>

  <!-- Postcard -->
  <section class="abs postcard">
    <svg class="abs field" width="600" height="390" viewBox="0 0 600 390"><path d="M0 0H348L292 390H0Z" fill="var(--green)"/></svg>
    <h2 class="abs title" style="left:23px;top:24px">LOWER YOUR KDP MORTGAGE<br>PAYMENT RIGHT NOW</h2>
    <div class="abs req-head">The Quickpath process requires</div>
    <span class="abs no" style="left:22px;top:120px;font-size:70px">NO</span>
    <ul class="abs checks" style="left:84px;top:122px;width:162px">
      <li style="font-size:12px;height:18px">APPRAISAL<svg width="10" height="10" viewBox="0 0 9 9"><rect x=".5" y=".5" width="8" height="8" fill="#fff" stroke="var(--green-dark)"/><path d="M2 4.5l2 2 3-4" stroke="var(--green-dark)" fill="none" stroke-width="1.3"/></svg></li>
      <li style="font-size:12px;height:18px">INCOME VERIFICATION<svg width="10" height="10" viewBox="0 0 9 9"><rect x=".5" y=".5" width="8" height="8" fill="#fff" stroke="var(--green-dark)"/><path d="M2 4.5l2 2 3-4" stroke="var(--green-dark)" fill="none" stroke-width="1.3"/></svg></li>
      <li style="font-size:12px;height:18px">ASSET DOCUMENTATION<svg width="10" height="10" viewBox="0 0 9 9"><rect x=".5" y=".5" width="8" height="8" fill="#fff" stroke="var(--green-dark)"/><path d="M2 4.5l2 2 3-4" stroke="var(--green-dark)" fill="none" stroke-width="1.3"/></svg></li>
      <li style="font-size:12px;height:18px">OUT OF POCKET CLOSING COSTS.<svg width="10" height="10" viewBox="0 0 9 9"><rect x=".5" y=".5" width="8" height="8" fill="#fff" stroke="var(--green-dark)"/><path d="M2 4.5l2 2 3-4" stroke="var(--green-dark)" fill="none" stroke-width="1.3"/></svg></li>
    </ul>

    <div class="abs means-head">What this means<br>to you is:</div>
    <ul class="abs means cond">
      <li><svg width="12" height="9" viewBox="0 0 14 10"><path d="M0 5h9M6 1l4 4-4 4" stroke="#fff" stroke-width="2.4" fill="none"/></svg>A REDUCTION IN MONTHLY PAYMENT</li>
      <li><svg width="12" height="9" viewBox="0 0 14 10"><path d="M0 5h9M6 1l4 4-4 4" stroke="#fff" stroke-width="2.4" fill="none"/></svg>POSSIBILITY TO SKIP FIRST TWO<br>MORTGAGE PAYMENTS</li>
      <li><svg width="12" height="9" viewBox="0 0 14 10"><path d="M0 5h9M6 1l4 4-4 4" stroke="#fff" stroke-width="2.4" fill="none"/></svg>SAME TYPE OF 30 YEAR<br>FIXED RATE LOAN – BACKED BY THE KDP</li>
    </ul>

    <div class="abs note" style="left:145px;top:203px;width:152px;height:142px;padding:22px 8px 0 12px;transform:rotate(-6deg)">
      <svg class="pin" width="20" height="24" viewBox="0 0 20 24"><circle cx="9" cy="9" r="8" fill="var(--pin)"/><path d="M9 16l-3 8" stroke="#888" stroke-width="1.5"/></svg>
      <div class="firm">Quillan Mortgage</div>
      <p>418 Garnet Avenue, Suite 1450<br>Seattle, WA 98344<br>Office 206 555 0143<br>Fax 206 555 0187<br>Email quickpath@quillanmortgage.com</p>
      <div class="staff">Tom Wendell <small>- Vice President - MLO-31947</small><br>Leo Marsh <small>- Loan Originator</small></div>
    </div>

    <div class="abs brand" style="left:358px;top:32px"><i></i>Quillan</div>
    <div class="abs badge" style="left:357px;top:72px;width:50px;height:20px"></div>
    <div class="abs stamp"></div>
    <div class="abs addr-line" style="top:183px"></div>
    <div class="abs addr-line" style="top:241px"></div>
    <div class="abs addr-line" style="top:299px"></div>
  </section>

</div>
</body>
</html>
```